Gift Card Design - Suds Harbor Co

I am needing a design for a standard plastic gift card, (ever so slightly large then a standard rounded edge business card). Name of the business is Suds Harbor Co. Attached is a file with a poor example, done by an equipment manufacturing firm, that I feel could be much better. Simple, clean and classy with what it is and does along with our name is what I am looking for. Attached also is out logo and source of logo, they don't have to be on the card.

Target Market(s)

Car wash customers in an upscale market.

Industry/Entity Type

Business

Font styles to use
Serif
Other font styles liked:
• whatever you feel, but I do like the font on a Brevanto golf ball

Requirements
Must have
• Words anywhere on the card -
• Reloadable Card
• Self Serve Bays & Vacuums.
• Also need name of the business, Suds Harbor Co.
Nice to have
• Work in Pantone #7483 as there is existing signage with that as a primary color, just trying to tie things together. Attached is my business logo and a picture of the source of the logo, you do not have to use those if you don't want to. I do like clean and classy but am open to creativity, that's why I am submitting this project.
Should not have
• Naked lady pictures

```html
<!DOCTYPE html>
<html lang="en">
<head>
<meta charset="utf-8">
<title>Suds Harbor Co – Reloadable Gift Card</title>
<link rel="stylesheet" href="https://fonts.googleapis.com/css2?family=Nunito:wght@600;700;800&display=swap">
<style>
  :root {
    --backdrop: #8c8c8c;
    --copper-light: #f0a67a;
    --copper: #d98a5c;
    --copper-dark: #a8623c;
    --teal-light: #137a92;
    --teal: #0e6479;
    --teal-dark: #0a4f61;
    --ink-light: #f3e6ee;
    --title-shadow: #17343f;
  }
  * { margin: 0; padding: 0; box-sizing: border-box; }
  html, body {
    width: 1200px;
    height: 928px;
    overflow: hidden;
    background: var(--backdrop);
  }
  .stage {
    width: 1200px;
    height: 928px;
    display: flex;
    align-items: center;
    justify-content: center;
  }
  .gift-card {
    position: relative;
    width: 760px;
    height: 480px;
    border-radius: 24px;
    overflow: hidden;
    box-shadow: 0 18px 40px rgba(0, 0, 0, 0.28);
    font-family: "Nunito", sans-serif;
  }
  .card-bands {
    position: absolute;
    inset: 0;
    width: 100%;
    height: 100%;
  }
  .brand-mark {
    position: absolute;
    left: 50%;
    top: 112px;
    transform: translateX(-50%);
    display: flex;
    align-items: center;
    gap: 14px;
  }
  .brand-mark__dot {
    width: 30px;
    height: 30px;
    border-radius: 50%;
    border: 3px solid var(--ink-light);
  }
  .brand-mark__name {
    font-size: 30px;
    font-weight: 700;
    color: var(--ink-light);
    letter-spacing: 0.02em;
    white-space: nowrap;
  }
  .card-features {
    position: absolute;
    left: 405px;
    top: 238px;
    color: var(--ink-light);
    font-weight: 600;
    font-size: 21px;
    line-height: 1.15;
  }
  .card-title {
    position: absolute;
    left: 64px;
    top: 318px;
    font-size: 74px;
    font-weight: 800;
    color: var(--ink-light);
    letter-spacing: 0.01em;
    text-shadow: 4px 4px 0 var(--title-shadow);
    white-space: nowrap;
  }
</style>
</head>
<body>
  <main class="stage">
    <article class="gift-card">
      <svg class="card-bands" viewBox="0 0 760 480" preserveAspectRatio="none" aria-hidden="true">
        <defs>
          <linearGradient id="copperBand" x1="0" y1="1" x2="1" y2="0">
            <stop offset="0" stop-color="var(--copper-dark)"/>
            <stop offset="0.55" stop-color="var(--copper)"/>
            <stop offset="0.75" stop-color="var(--copper-light)"/>
            <stop offset="1" stop-color="var(--copper)"/>
          </linearGradient>
          <linearGradient id="tealBand" x1="0" y1="0" x2="1" y2="1">
            <stop offset="0" stop-color="var(--teal-dark)"/>
            <stop offset="0.6" stop-color="var(--teal-light)"/>
            <stop offset="1" stop-color="var(--teal)"/>
          </linearGradient>
        </defs>
        <rect class="band band--teal" x="0" y="0" width="760" height="480" fill="url(#tealBand)"/>
        <polygon class="band band--copper" points="0,0 760,0 760,190 0,300" fill="url(#copperBand)"/>
      </svg>

      <div class="brand-mark">
        <span class="brand-mark__dot"></span>
        <span class="brand-mark__name">Suds Harbor Co</span>
      </div>

      <p class="card-features">
        Reloadable Card<br>
        Self Serve Bays &amp; Vacuums
      </p>

      <h1 class="card-title">Suds Harbor Co</h1>
    </article>
  </main>
</body>
</html>
```